New Business Aquisition Postcard Project

Create a post card for new client acquisition. The postcard is to promote our new campaign, our SAVE YOU OR SEND YOU MONEY Campaign. We have preselected people that we know we are highly likely to save money. These people own homes, valued 100k or over, these homes were built after the year 2000 and are within a radius of our office. If we cannot save them $307 (the average savings experienced by our customers) a year on their home and auto insurance combined, we will send them a $20 gift card for wasting their time.

Target Market(s)

This mailing will be sent to confirmed homeowners in Western Pennsylvania. These people own a home built after the year 2000.

Industry/Entity Type

Car Insurance

Font styles to use
Serif

Colors
0355a3

Requirements
Must have
• I have included a picture of the flyer I created. We need to include testimonials. I have those on the flyer and more.
Nice to have
• This should be laid out and ready to go in a postcard format. I have not decided if I will use labels or just run the postcards through my printer to put the names on. Where the flyer uses a person's name, the postcard should use "Pennsylvania Homeowner". It could also say "Attention to Pennsylvania Homeowners with homes built after the year 2000." Remember, we have preselected this people and we can let them know that. This offer will only be going to highly qualified prospects and will not be plastered all over town, so to speak.

```html
<!DOCTYPE html>
<html lang="en">
<head>
<meta charset="utf-8">
<title>Save You or Send You Money Postcard</title>
<link href="https://fonts.googleapis.com/css2?family=Lora:ital,wght@0,400;0,700;1,400&family=Oswald:wght@600;700&display=swap" rel="stylesheet">
<style>
:root{
  --blue:#0355a3;
  --ink:#1c1c1c;
  --muted:#555;
  --paper:#ffffff;
  --bg:#e9ebee;
  --pale:#eef3f9;
  --line:#cdd9e6;
}
*{box-sizing:border-box;margin:0;padding:0}
html,body{width:900px;height:1200px;overflow:hidden;background:var(--bg);font-family:"Lora",serif;color:var(--ink)}
.card{position:absolute;left:30px;width:840px;height:525px;background:var(--paper);box-shadow:0 4px 14px rgba(0,0,0,.25);overflow:hidden;display:flex}
.card.front{top:45px}
.card.back{top:615px}
.half{position:relative;width:420px;height:100%}
.band{position:absolute;left:0;right:0;height:14px;background:var(--blue)}
.band.top{top:0}.band.bottom{bottom:0}
.band::after{content:"";position:absolute;left:0;right:0;height:2px;background:var(--paper)}
.band.top::after{bottom:4px}.band.bottom::after{top:4px}
.logo{font-weight:700;color:var(--blue);font-size:30px;letter-spacing:-.5px;display:flex;align-items:center;gap:8px}
.logo .mark{width:12px;height:12px;background:var(--blue)}
.letter{padding:30px 28px 28px}
.letter .logo{margin-bottom:18px}
.merge{font-size:10.5px;line-height:1.5;margin-bottom:12px}
.lead{font-size:12px;font-weight:700;color:var(--blue);line-height:1.4;margin-bottom:10px}
.body{font-size:9.6px;line-height:1.6;color:var(--muted);margin-bottom:9px}
.body strong{color:var(--ink)}
.bigline{font-size:12px;font-weight:700;line-height:1.35;margin:6px 0 10px}
.bigline span{color:var(--blue)}
.offer{padding:22px 24px 0;border-left:1px solid #ddd}
.headline{font-family:"Oswald",sans-serif;font-weight:700;font-size:50px;line-height:1;letter-spacing:.5px;text-align:center}
.headline.second{background:var(--blue);color:var(--paper);padding:4px 0 6px;margin:4px 0 14px}
.offer .body{text-align:center;font-size:10px}
.rates{background:var(--blue);color:var(--paper);text-align:center;padding:16px 12px;margin:12px 0 16px}
.rates h3{font-size:21px;font-weight:700;margin-bottom:6px}
.rates p{font-size:12px;font-weight:700;line-height:1.4}
.rates .pay{font-size:24px;margin-top:6px}
.guarantee{font-size:11.5px;font-weight:700;text-align:center;margin-bottom:8px}
.webbar{position:absolute;left:0;right:0;bottom:0;background:var(--blue);color:var(--paper);text-align:center;padding:13px 0;font-size:11.5px;line-height:1.5}
.webbar b{font-size:14px}
.testi{background:var(--pale);padding:22px 20px 0;height:100%}
.testi h4{font-size:14px;font-weight:700;color:var(--blue);margin-bottom:10px;letter-spacing:.5px}
.quote{display:flex;gap:10px;background:var(--paper);border:1px solid var(--line);padding:9px;margin-bottom:10px}
.quote .photo{flex:0 0 66px;height:66px;background:linear-gradient(135deg,#c9b6a3,#8c7a6b)}
.quote p{font-size:9.4px;line-height:1.5;font-style:italic;color:var(--muted)}
.quote cite{display:block;text-align:right;font-size:9px;color:var(--blue);font-style:normal;margin-top:4px}
.dear{font-size:9.6px;line-height:1.6;color:var(--muted);margin:8px 0}
.dear b{color:var(--ink)}
.boxes{display:flex;gap:8px;margin-top:8px}
.gift{flex:1;background:var(--blue);color:var(--paper);padding:10px}
.gift h5{font-size:12px;text-align:center;margin-bottom:6px}
.gift p{font-size:8.8px;line-height:1.5}
.call{flex:1;border:2px solid var(--blue);background:var(--paper);padding:10px;font-size:8.8px;line-height:1.5;color:var(--muted)}
.call h5{font-size:11px;color:var(--blue);text-align:center;margin-bottom:6px}
.mailing{padding:46px 30px}
.mailing .logo{font-size:26px}
.contact{margin-top:16px;font-size:12px;line-height:1.5}
.contact .row{display:flex;align-items:flex-start;gap:8px;margin-bottom:6px}
.contact svg{flex:0 0 16px;margin-top:2px}
.stamp{position:absolute;top:40px;right:30px;width:64px;height:74px;border:1.5px dashed var(--blue)}
</style>
</head>
<body>

<section class="card front">
  <div class="half">
    <div class="band top"></div>
    <div class="letter">
      <div class="logo"><span class="mark"></span>Marlow Reed Agency</div>
      <div class="merge">July 30, 2016<br>«First_Name» «Last_Name»<br>«Street_Address»<br>«City», «State» «Zip»<br>Dear «First_Name»:</div>
      <p class="lead">Congratulations «First_Name»!! You and your family will be SAFE AND WEALTHIER just by reading this letter…</p>
      <p class="body">As a Pennsylvania homeowner with a home built after the year 2000, you were preselected for this offer. We know we are highly likely to lower what you pay, and we want to prove it to you with a quick, no‑pressure review of your home and auto policies.</p>
      <p class="bigline">Our insurance agency is different… <span>And the difference will better protect you!</span></p>
      <p class="body">For over a decade our family‑owned office has helped neighbors in Western Pennsylvania keep more of their money while getting stronger coverage. This mailing goes only to a small group of highly qualified homeowners, so it will not be seen all over town.</p>
      <p class="body">Call us today or visit our website to request your free quote. It takes only a few minutes, and you have nothing to lose. <strong>Either we save you money, or we send you money.</strong></p>
    </div>
    <div class="band bottom"></div>
  </div>

  <div class="half offer">
    <div class="headline">SAVE YOU OR</div>
    <div class="headline second">SEND YOU MONEY</div>
    <p class="body">Our customers save an average of $307 per year when they combine their home and auto insurance with us. We are confident we can do the same for you and your family.</p>
    <div class="rates">
      <h3>Our NEW Rates are So Low…</h3>
      <p>If I Can't Save You AT LEAST $307.00 Per Year on Your Auto and Home Insurance,</p>
      <p class="pay">I'll Pay You $20.00!*</p>
    </div>
    <p class="guarantee">I Guarantee to SAVE YOU OR SEND YOU MONEY…. PERIOD</p>
    <p class="body">No tricks and no obligation. If we cannot beat your current rate by at least $307 a year, a $20 gift card is yours for your time. *One gift card per household.</p>
    <div class="webbar">For more info please visit our website<br><b>www.quotemarlow.com</b></div>
  </div>
</section>

<section class="card back">
  <div class="half">
    <div class="testi">
      <h4>TESTIMONIALS:</h4>
      <div class="quote">
        <div class="photo" role="img" aria-label="Portrait photo of a satisfied customer"></div>
        <div><p>"The team took the time to review every policy we had and found us better coverage for less. We saved far more than we expected and the service has been friendly from day one."</p><cite>— Dana Whitford</cite></div>
      </div>
      <div class="quote">
        <div class="photo" role="img" aria-label="Portrait photo of a satisfied customer"></div>
        <div><p>"When our agent said they could beat our rate we were skeptical, but they did it in one phone call. Bundling our home and auto was easy and we now recommend them to all of our friends."</p><cite>— Paula Renner</cite></div>
      </div>
      <p class="dear"><b>Dear Owner,</b> every customer is treated like family. We answer our phones, we review your policies every year, and we are right here in Western Pennsylvania when you need us most.</p>
      <div class="boxes">
        <div class="gift"><h5>FREE $20 Gift Card</h5><p>Request your free quote today. If we can't save you at least $307 a year on home and auto combined, we send you a $20 gift card.</p></div>
        <div class="call"><h5>CALL TODAY AT</h5>(555) 410-2286 for a free review of your home and auto policies. Offer limited to preselected homeowners.</div>
      </div>
    </div>
    <div class="webbar">For more info please visit our website<br><b>marlowreed.com &nbsp;|&nbsp; www.quotemarlow.com</b></div>
  </div>

  <div class="half mailing">
    <div class="band top"></div>
    <div class="logo"><span class="mark"></span>Marlow Reed Agency</div>
    <div class="contact">
      <div class="row">
        <svg width="16" height="18" viewBox="0 0 16 18"><path d="M8 1a5.5 5.5 0 0 0-5.5 5.5C2.5 11 8 17 8 17s5.5-6 5.5-10.5A5.5 5.5 0 0 0 8 1z" fill="#0355a3"/><circle cx="8" cy="6.5" r="2" fill="#fff"/></svg>
        <span>418 Birchwood Lane<br>Greenfield, PA 15000</span>
      </div>
      <div class="row">
        <svg width="16" height="16" viewBox="0 0 16 16"><path d="M3.5 1.5l2.5 0 1.2 3.2-1.6 1.2a8 8 0 0 0 4.5 4.5l1.2-1.6 3.2 1.2v2.5c0 .8-.7 1.5-1.5 1.5C6.9 14 2 9.1 2 3c0-.8.7-1.5 1.5-1.5z" fill="#0355a3"/></svg>
        <span>(555) 410-2286</span>
      </div>
      <div class="row">
        <svg width="16" height="16" viewBox="0 0 16 16"><rect x="2" y="3" width="12" height="10" rx="1" fill="#0355a3"/><rect x="4" y="5" width="8" height="3" fill="#fff"/></svg>
        <span>(555) 410-2290</span>
      </div>
    </div>
    <div class="stamp"></div>
    <div class="band bottom"></div>
  </div>
</section>

</body>
</html>
```